Power Point Presentation to Large Audience

Make a consistent look and feel but also make it a compelling presentation. I have attached a summary of my presentation

Target Market(s)

I am making a presentation to investors. Need a consistent look feel but I need it to be simple in design

Requirements
Must have
• Use http://brightlane4jobs.example/ for any background into the company
Nice to have
• My presentation has to be short, less than 10 to 15 minutes. The format I have attached is my basic content, I need it cleaned up and put in a compelling format

```html
<!DOCTYPE html>
<html lang="en">
<head>
<meta charset="utf-8">
<title>Brightlane 4 Jobs – Investor Deck, First Part</title>
<link href="https://fonts.googleapis.com/css2?family=Arimo:wght@400;700&display=swap" rel="stylesheet">
<style>
:root{
  --orange:#f7941d;
  --ink:#3b3b3b;
  --text:#555;
  --footer:#6f6f70;
  --canvas:#ebebeb;
  --white:#fff;
}
*{box-sizing:border-box;margin:0;padding:0}
html,body{width:1200px;height:1200px;overflow:hidden;background:var(--canvas);font-family:"Arimo",Arial,sans-serif;color:var(--ink)}
.slide{position:absolute;width:573px;height:323px;background:var(--white);overflow:hidden}
.s1{left:19px;top:22px;height:314px}
.s2{left:608px;top:22px;height:322px}
.s3{left:19px;top:362px}
.s4{left:610px;top:362px;width:571px}
.s5{left:19px;top:702px}
.s6{left:610px;top:702px;width:571px}

.brand{position:absolute;display:flex;align-items:center;gap:4px;color:var(--orange);font-weight:700;white-space:nowrap}
.brand .dot{width:8px;height:8px;background:var(--orange)}
.brand-lg{left:19px;top:40px;font-size:9.5px}
.brand-sm{right:19px;top:33px;font-size:6px}
.brand-sm .dot{width:6px;height:6px}

.title{position:absolute;left:18px;top:26px;font-size:17px;font-weight:700;color:var(--ink)}

.footer{position:absolute;left:0;right:0;bottom:0;height:18px;background:var(--footer);color:#eee;font-size:5.5px;display:flex;align-items:center;padding-left:18px}
.footer .tag{position:absolute;right:0;top:0;height:18px;display:flex}
.footer .ns{width:62px;background:var(--white);color:var(--footer);font-size:8px;display:flex;align-items:center;justify-content:center}
.footer .num{width:38px;background:var(--orange);color:#fff;font-size:5px;display:flex;align-items:center;justify-content:center}

/* slide 1 */
.road{position:absolute;left:0;top:70px;width:100%;height:245px;background:linear-gradient(#8a6a4a 0%,#a98a63 40%,#9a7a45 62%,#3a3a3a 100%)}
.quote{position:absolute;left:0;right:0;top:134px;text-align:center;color:#fff;font-size:18.5px;line-height:24px}
.quote-by{position:absolute;left:0;right:0;top:206px;text-align:center;color:#fff;font-size:12px;padding-left:30px}

/* slide 2 */
.question{position:absolute;left:18px;top:152px;font-size:22px;line-height:27.5px;color:var(--ink)}
.question b{color:var(--orange);font-weight:700}
.study{position:absolute;left:272px;top:0;width:301px;height:100%;background:linear-gradient(135deg,#c9c3b9,#8f7f6d 60%,#d9cdb8);border-left:8px solid #7a7a7a}

/* slide 3 */
.students{position:absolute;left:0;top:60px;width:248px;height:229px;background:linear-gradient(135deg,#7ab9c9,#c89b7b 55%,#8c3b3b)}
.block{position:absolute;left:276px;width:270px}
.block h3{font-size:12px;font-weight:700;color:var(--ink);margin-bottom:9px}
.block .row{display:flex;gap:9px;font-size:8.2px;line-height:11.6px;color:var(--text)}
.block .row svg{flex:none}
.hl{color:var(--orange);font-weight:700}

/* slide 4 */
.col{position:absolute;text-align:center;font-size:8.4px;line-height:11.5px;color:var(--text)}
.col svg{position:absolute;left:50%;top:0;margin-left:-39px}
.col p{position:absolute;left:0;right:0;top:95px}
.col-left{left:52px;width:194px;top:92px;height:160px}
.col-right{left:332px;width:184px;top:92px;height:160px}
.divider{position:absolute;left:286px;top:70px;width:1px;height:220px;background:#ddd}

/* slide 5 */
.laptop{position:absolute;left:123px;top:61px;width:327px;height:214px;background:#1d1d1d;border-radius:10px}
.screen{position:absolute;left:12px;top:15px;width:302px;height:190px;background:#fff}
.base{position:absolute;left:84px;top:268px;width:405px;height:8px;background:linear-gradient(#d6d6d6,#9a9a9a);border-radius:0 0 40px 40px}

/* slide 6 */
.school{position:absolute;inset:0;background:linear-gradient(#5a554d,#3f3b35 55%,#5b564e)}
.stat{position:absolute;left:18px;top:210px;color:#fff;font-size:24px;line-height:29px}
.source{position:absolute;left:18px;top:302px;color:#ddd;font-size:5.5px}

.part{position:absolute;left:20px;top:1090px;font-size:60px;font-weight:700;color:#000;letter-spacing:1px}
</style>
</head>
<body>

<section class="slide s1">
  <div class="brand brand-lg"><span class="dot"></span>BRIGHTLANE 4 JOBS</div>
  <div class="road" role="img" aria-label="Photo of an open desert road stretching to the horizon under a dusky sky"></div>
  <p class="quote">“To find out what one is fitted to do, and to secure an<br>opportunity to do it, is the key to happiness.”</p>
  <p class="quote-by">— Mara Ellison</p>
</section>

<section class="slide s2">
  <svg style="position:absolute;left:18px;top:78px" width="66" height="56" viewBox="0 0 66 56" fill="none" stroke="#f7941d" stroke-width="3">
    <path d="M4 10v38h24l4 4 4-4h26V10"/><path d="M10 4v38h20l2 3V8l-4-4z"/><path d="M58 4v20M34 8l4-4h20"/>
    <circle cx="45" cy="30" r="9"/><path d="M51 37l9 9"/>
  </svg>
  <p class="question">Has <b>personalized<br>learning</b> has gotten<br>it wrong?</p>
  <div class="study" role="img" aria-label="Photo of a tired student reading at a library table beside a stack of books"></div>
</section>

<section class="slide s3">
  <h2 class="title">Personalized Learning Model</h2>
  <div class="brand brand-sm"><span class="dot"></span>BRIGHTLANE 4 JOBS</div>
  <div class="students" role="img" aria-label="Photo of smiling students writing at their desks in a classroom"></div>
  <div class="block" style="top:78px">
    <h3>Personalized Learning Model Definition</h3>
    <div class="row">
      <svg width="29" height="30" viewBox="0 0 29 30" fill="none" stroke="#f7941d" stroke-width="1.6"><path d="M8 29v-6c-4-3-6-6-6-11C2 6 7 2 13 2s11 4 11 10l3 5h-3v5h-5v7"/><circle cx="14" cy="12" r="4"/><path d="M14 5v3M14 16v3M7 12h3M18 12h3"/></svg>
      <p>Personalized-learning models seek to adapt the pace of learning and the instructional strategies being used to best fit each individual child's strengths, weaknesses, and <b>interests.</b></p>
    </div>
  </div>
  <div class="block" style="top:176px">
    <h3>Personalized Learning Results</h3>
    <div class="row">
      <svg width="29" height="30" viewBox="0 0 29 30" fill="none" stroke="#f7941d" stroke-width="1.6"><rect x="3" y="2" width="23" height="26" rx="2"/><path d="M3 23h23M8 8h13v5H8z"/></svg>
      <p><span class="hl">"The evidence base is very weak at this point,"</span> said <b>Tobias R. Venn</b>, a senior scientist and the group's distinguished chair in education innovation.</p>
    </div>
  </div>
  <div class="footer">QV7learn™ &nbsp; Brightlane4Jobs™ &nbsp; 2018 Trademark QV7learn, LLC
    <div class="tag"><span class="ns">QV7learn</span><span class="num">3</span></div></div>
</section>

<section class="slide s4">
  <h2 class="title">Where has it Gone Wrong?</h2>
  <div class="brand brand-sm"><span class="dot"></span>BRIGHTLANE 4 JOBS</div>
  <div class="col col-left">
    <svg width="78" height="78" viewBox="0 0 78 78" fill="none" stroke="#f7941d" stroke-width="1.6"><circle cx="39" cy="39" r="38"/><path d="M30 62v-8c-5-4-7-8-7-13 0-9 7-15 16-15s15 6 15 14l4 6h-4v6h-6v10" stroke="#555"/><circle cx="44" cy="29" r="5" stroke="#555"/><path d="M44 20v3M44 35v3M35 29h3M50 29h3" stroke="#555"/></svg>
    <p>Many versions of <b>personalized learning seek</b> to change or replace fundamental processes that shape the <b>day-to-day life of schools</b>—everything from how teachers prepare lessons to how students are graded.</p>
  </div>
  <div class="divider"></div>
  <div class="col col-right">
    <svg width="78" height="78" viewBox="0 0 78 78" fill="none" stroke="#f7941d" stroke-width="1.6"><circle cx="39" cy="39" r="38"/><g stroke="#555"><path d="M32 50c0-6-6-8-6-16a13 13 0 0 1 26 0c0 8-6 10-6 16z"/><path d="M33 54h12M34 58h10M39 50V38l-4-4M39 38l4-4M39 14v-4M22 20l-3-3M56 20l3-3M16 34h-4M62 34h4"/></g></svg>
    <p><b>HINT:</b> We weren't doing that well to begin with, replicating what doesn't work <b>into personalized learning plans</b> doesn't change behaviour</p>
  </div>
  <div class="footer">QV7learn™ &nbsp; Brightlane4Jobs™ &nbsp; 2018 Trademark QV7learn, LLC
    <div class="tag"><span class="ns">QV7learn</span><span class="num">4</span></div></div>
</section>

<section class="slide s5">
  <h2 class="title">NSAM Math Scores</h2>
  <div class="brand brand-sm"><span class="dot"></span>BRIGHTLANE 4 JOBS</div>
  <div class="laptop">
    <div class="screen">
      <svg width="302" height="190" viewBox="0 0 302 190" font-family="Arimo, Arial, sans-serif">
        <text x="151" y="13" font-size="5" fill="#1e4f8f" text-anchor="middle" font-weight="700">Figure 1: NSAM math score trends for grades 4 and 8</text>
        <g stroke="#bbb" stroke-width="0.5">
          <line x1="55" y1="25" x2="282" y2="25"/><line x1="55" y1="57.8" x2="282" y2="57.8"/><line x1="55" y1="90.5" x2="282" y2="90.5"/><line x1="55" y1="114" x2="282" y2="114"/><line x1="55" y1="130" x2="282" y2="130" stroke="#666"/>
        </g>
        <g font-size="4" fill="#555"><text x="48" y="27">0.8</text><text x="48" y="59">0.6</text><text x="48" y="92">0.4</text><text x="48" y="116">0.2</text><text x="48" y="132">0.0</text></g>
        <polyline fill="none" stroke="#1f6fb5" stroke-width="1.2" points="55,130 77.5,122.1 100,119.5 122.5,80.2 145,71 167.5,61.9 190,61.9 212.5,56.6 235,54 257.5,61.9 280,61.9"/>
        <polyline fill="none" stroke="#29a8df" stroke-width="1.2" points="55,130 77.5,123.5 100,118.2 122.5,102.5 145,98.6 167.5,92 190,84.2 212.5,81.5 235,77.6 257.5,88.1 280,84.2"/>
        <g font-size="4" fill="#333" text-anchor="middle">
          <text x="55" y="126">0.00</text><text x="77.5" y="118">0.06</text><text x="100" y="115">0.08</text><text x="122.5" y="76">0.38</text><text x="145" y="67">0.45</text><text x="167.5" y="58">0.52</text><text x="190" y="58">0.52</text><text x="212.5" y="53">0.56</text><text x="235" y="50">0.58</text><text x="257.5" y="58">0.52</text><text x="280" y="58">0.52</text>
          <text x="122.5" y="99">0.21</text><text x="145" y="95">0.24</text><text x="167.5" y="88">0.29</text><text x="190" y="81">0.35</text><text x="212.5" y="78">0.37</text><text x="235" y="74">0.40</text><text x="257.5" y="85">0.32</text><text x="280" y="81">0.35</text>
          <text x="151" y="160">Year</text>
        </g>
        <g font-size="3.5" fill="#555"><text x="55" y="145">1990</text><text x="100" y="145">2000</text><text x="145" y="145">2005</text><text x="190" y="145">2009</text><text x="235" y="145">2013</text><text x="280" y="145">2017</text></g>
        <g font-size="4" fill="#555"><line x1="110" y1="171" x2="120" y2="171" stroke="#1f6fb5"/><text x="122" y="172.5">Grade 4</text><line x1="190" y1="171" x2="200" y2="171" stroke="#29a8df"/><text x="202" y="172.5">Grade 8</text>
          <text x="8" y="183" font-size="3.5">Source: Author's calculations based on NSAM data.</text></g>
        <text x="282" y="186" font-size="11" fill="#1e4f8f" text-anchor="end" font-family="Georgia, serif">HALVERTON</text>
      </svg>
    </div>
  </div>
  <div class="base"></div>
  <div class="footer">QV7learn™ &nbsp; Brightlane4Jobs™ &nbsp; 2018 Trademark QV7learn, LLC
    <div class="tag"><span class="ns">QV7learn</span><span class="num">5</span></div></div>
</section>

<section class="slide s6">
  <div class="school" role="img" aria-label="Muted photo of teenagers skateboarding in front of a large brick high school"></div>
  <p class="stat">Nationwide, there are <b>2,397 high schools,</b><br>that do not graduate one-third or more<br>of their students.</p>
  <p class="source">Source: http://www.gradreport.example/files/annual_report_2016_final.pdf (accessed August 25, 2016)</p>
</section>

<h1 class="part">FIRST PART</h1>

</body>
</html>
```